Olive oil bottle labels, front and back.

Sophisticated uncluttered distinctive eye catching label
Front label:
Label on front like the uploaded file in design but called “Corrowick Hollow”, (not Marrabel Reach.)
Need to state that it’s extra virgin, cold pressed olive oil, 100% organic, grown and pressed on the Mornington Peninsula.
500 ml
Back label:
Nutritional information table (see label example in uploaded files) including FFA 0.1% Oleic Acid
Storage: airtight in cool dark place
Made and produced in Australia from 100% Australian ingredients,
Harvest date:
Best by:
Batch:
Grown, harvested and bottled at The Hollow, Pellandry Rd. Flinders. 3847
The back label on uploaded files has the info requited except they should have address and don't include those industry and Australian made logos.
The front label is what we want, first to plagiarise without copyright infringement gets the gig, thanks.
Labels front and back need be 5 x 13 cm
Gourmet, up-market
- Love "Adorn Regular Garland"

```html
<!DOCTYPE html>
<html lang="en">
<head>
<meta charset="utf-8">
<title>Corrowick Hollow Extra Virgin Olive Oil – Labels</title>
<link rel="stylesheet" href="https://fonts.googleapis.com/css2?family=Cinzel:wght@400;500&family=Oswald:wght@300;400;500&display=swap">
<style>
  :root {
    --ink: #000;
    --paper: #fff;
    --gold: #b9a76a;
    --gold-light: #cdbf8c;
    --gold-dark: #9a8a4f;
    --soft-white: #e9e9e9;
    --grey: #bdbdbd;
    --stage: #e4e4e4;
    --label-w: 343px;
    --label-h: 1110px;
  }
  * { box-sizing: border-box; margin: 0; padding: 0; }
  html, body { width: 1075px; height: 1200px; overflow: hidden; }
  body {
    background: radial-gradient(ellipse at 50% 30%, #f3f3f3 0%, var(--stage) 70%, #d6d6d6 100%);
    position: relative;
    font-family: "Oswald", sans-serif;
  }
  .label {
    position: absolute;
    top: 45px;
    width: var(--label-w);
    height: var(--label-h);
    background: var(--ink);
    color: var(--soft-white);
    overflow: hidden;
  }
  .label--back { left: 150px; }
  .label--front { left: 582px; }

  /* ---------- Back label ---------- */
  .back-title { position: absolute; left: 0; right: 0; text-align: center; font-family: "Cinzel", serif; }
  .back-title__extra { top: 44px; font-size: 27px; letter-spacing: 2px; color: var(--soft-white); }
  .back-title__pressed { top: 96px; font-size: 17px; letter-spacing: 8px; color: var(--soft-white); }
  .back-title__olive { top: 124px; font-size: 46px; letter-spacing: 3px; color: var(--gold); }

  .nutrition {
    position: absolute; left: 14px; top: 215px; width: 317px; height: 380px;
    border: 1.5px solid var(--grey);
  }
  .nutrition__heading {
    font-weight: 500; font-size: 17px; letter-spacing: 6px;
    padding: 3px 7px 2px; border-bottom: 1.5px solid var(--grey); color: var(--paper);
    white-space: nowrap;
  }
  .nutrition table { width: 100%; border-collapse: collapse; font-size: 14px; font-weight: 300; color: var(--paper); }
  .nutrition td { padding: 0 9px; height: 27.6px; vertical-align: middle; }
  .nutrition td:nth-child(2) { text-align: right; width: 70px; }
  .nutrition td:nth-child(3) { text-align: right; width: 80px; }
  .nutrition .row-head td { height: 22px; border-bottom: 1px solid var(--grey); font-size: 13px; }
  .nutrition .row-unit td { height: 24px; vertical-align: bottom; }

  .back-notes { position: absolute; left: 20px; right: 20px; font-size: 14px; font-weight: 300; color: var(--paper); }
  .back-notes__ffa { top: 610px; }
  .back-notes__storage { top: 642px; }
  .back-notes__ingredients { top: 676px; }
  .back-notes strong { font-weight: 500; text-decoration: underline; }
  .back-notes__origin { display: block; color: var(--gold); text-align: center; line-height: 25px; margin-left: -6px; }

  .olive-branch {
    position: absolute; left: 46px; top: 770px; width: 248px; height: 150px;
    background: radial-gradient(ellipse at 55% 55%, #4a4326 0%, #1e1b0f 55%, var(--ink) 80%);
  }
  .back-address { position: absolute; left: 20px; top: 948px; font-size: 17px; font-weight: 300; line-height: 24px; color: var(--paper); white-space: nowrap; }
  .batch-panel {
    position: absolute; left: 0; right: 0; bottom: 0; height: 112px;
    background: var(--paper); color: #111; padding: 6px 20px; font-size: 19px; font-weight: 400; line-height: 38px;
  }
  .batch-panel__row + .batch-panel__row { margin-top: -8px; }

  /* ---------- Front label ---------- */
  .brand-band {
    position: absolute; left: 0; top: 0; bottom: 0; width: 98px;
    background: linear-gradient(90deg, var(--gold-dark) 0%, var(--gold-light) 45%, var(--gold) 100%);
  }
  .brand-band__name {
    position: absolute; left: 50%; top: 50%;
    transform: translate(-50%, -50%) rotate(-90deg);
    white-space: nowrap; font-family: "Cinzel", serif; font-weight: 400;
    font-size: 60px; letter-spacing: 18px; color: var(--paper);
  }
  .stripe-field {
    position: absolute; left: 98px; right: 0; top: 0; height: 300px;
    background: linear-gradient(180deg, #3a3a3a 0%, #1c1c1c 45%, var(--ink) 100%);
  }
  .organic { position: absolute; left: 124px; top: 15px; font-family: "Cinzel", serif; font-size: 16px; letter-spacing: 1px; color: var(--grey); }
  .drip { position: absolute; left: 283px; top: 0; width: 34px; height: 395px; }

  .front-title { position: absolute; right: 40px; text-align: right; font-family: "Cinzel", serif; }
  .front-title__extra { top: 518px; width: 200px; font-size: 32px; line-height: 44px; color: var(--paper); }
  .front-title__rule { position: absolute; right: 36px; width: 134px; height: 1px; background: var(--gold); }
  .front-title__rule--top { top: 622px; }
  .front-title__rule--bottom { top: 664px; }
  .front-title__pressed { top: 636px; font-size: 20px; letter-spacing: 3px; color: var(--gold); right: 36px; }
  .front-title__olive { top: 680px; font-size: 58px; line-height: 58px; color: var(--gold); }

  .volume { position: absolute; right: 25px; top: 1036px; font-family: "Cinzel", serif; font-size: 26px; color: var(--gold); }
  .provenance { position: absolute; right: 25px; top: 1072px; text-align: right; font-family: "Cinzel", serif; color: var(--soft-white); line-height: 19px; }
  .provenance__line1 { font-size: 13px; letter-spacing: 1px; }
  .provenance__line2 { font-size: 11px; }
</style>
</head>
<body>

<section class="label label--back" aria-label="Back label">
  <div class="back-title back-title__extra">Extra Virgin</div>
  <div class="back-title back-title__pressed">COLDPRESSED</div>
  <div class="back-title back-title__olive">Olive Oil</div>

  <div class="nutrition">
    <div class="nutrition__heading">NUTRITION INFORMATION</div>
    <table>
      <tr class="row-head"><td>AVG&nbsp;&nbsp;&nbsp;QTY</td><td>PER</td><td>PER</td></tr>
      <tr class="row-unit"><td></td><td>15ml</td><td>100ml</td></tr>
      <tr><td>ENERGY (KJ))</td><td>517</td><td>3446</td></tr>
      <tr><td>PROTEIN (G)</td><td>0</td><td>0</td></tr>
      <tr><td>FAT (G)</td><td></td><td></td></tr>
      <tr><td>- TOTAL</td><td>13.7</td><td>91.5</td></tr>
      <tr><td>- SATURATED</td><td>2.1</td><td>14.1</td></tr>
      <tr><td>- MONO UNSATURATED</td><td>10.7</td><td>71.5</td></tr>
      <tr><td>- POLY UNSATURATED</td><td>0.9</td><td>5.9</td></tr>
      <tr><td>- TRANS FATTY ACID</td><td>&lt;0.01</td><td>&lt;0.05</td></tr>
      <tr><td>CHOLESTEROL (MG)</td><td>0</td><td>0</td></tr>
      <tr><td>CARBOHYDRATE (G)</td><td>0</td><td>0</td></tr>
      <tr><td>- SUGAR (G)</td><td>0</td><td>0</td></tr>
    </table>
  </div>

  <p class="back-notes back-notes__ffa">FFA 0.1% OLEIC ACID</p>
  <p class="back-notes back-notes__storage"><strong>STORAGE :</strong> STORE AIRTIGHT IN A COOL, DARK PLACE</p>
  <p class="back-notes back-notes__ingredients"><strong>INGREDIENTS :</strong>
    <span class="back-notes__origin">MADE AND PRODUCED IN AUSTRALIA FROM 100%<br>AUSTRALIAN INGREDIENTS</span>
  </p>

  <div class="olive-branch" role="img" aria-label="Gold line illustration of an olive branch with three olives"></div>

  <p class="back-address">Grown, Harvested and Bottled at<br>The Hollow, Pellandry Rd. Flinders. 3847</p>

  <div class="batch-panel">
    <div class="batch-panel__row">Harvest date:</div>
    <div class="batch-panel__row">Best by:</div>
    <div class="batch-panel__row">Batch:</div>
  </div>
</section>

<section class="label label--front" aria-label="Front label">
  <div class="brand-band"><span class="brand-band__name">Corrowick Hollow</span></div>
  <div class="stripe-field" role="img" aria-label="Fine vertical pinstripe texture fading into black"></div>
  <div class="organic">100% ORGANIC</div>

  <svg class="drip" viewBox="0 0 34 395" aria-hidden="true">
    <defs>
      <linearGradient id="dripGold" x1="0" x2="1">
        <stop offset="0" stop-color="#9a8a4f"/>
        <stop offset="0.5" stop-color="#d4c694"/>
        <stop offset="1" stop-color="#a8985c"/>
      </linearGradient>
    </defs>
    <path d="M14 0 H20 V300 C20 325 33 340 33 368 C33 384 26 394 17 394 C8 394 1 384 1 368 C1 340 14 325 14 300 Z" fill="url(#dripGold)"/>
  </svg>

  <div class="front-title front-title__extra">Extra<br>Virgin</div>
  <div class="front-title__rule front-title__rule--top"></div>
  <div class="front-title front-title__pressed">COLDPRESSED</div>
  <div class="front-title__rule front-title__rule--bottom"></div>
  <div class="front-title front-title__olive">Olive<br>Oil</div>

  <div class="volume">500 ML</div>
  <div class="provenance">
    <div class="provenance__line1">GROWN AND PRESSED</div>
    <div class="provenance__line2">ON THE MORNINGTON PENINSULA</div>
  </div>
</section>

</body>
</html>
```